Fabulous Flyer for dream outdoor living construction and design company

we want a flyer designed to hand out at a large home show. We are a backyard dream design and build out company. come to us with or without your plans and we will build it for you. What makes us unique is that we have a 21,000 square foot showroom with lots of fountains, outdoor kitchens, grills, paver showroom, yard art, rock and much more for you to see, feel and buy amazing stuff... we carry 100's of top brand products like stonavo, kestrow, gray pellman and heatvista products. we build pergolas, outdoor kitchens, firepits, fireplaces, water features and more. our 3-d designs help you live it before you build it. but design is not our main function, construction is. solbrookyardhouse.example has a 3-d video on home page so you can see what we can do. Question...What do we put in a flyer that will invite people to our showroom, offer them free estimates, stress that we want to be chosen to do the build out, reqardless who designed it and most importantly that they are important to us. We are honored to be invited into their home to build their dream back yard. we do $2000 to $200,000 dreamscapes. How do we say that in a flyer??? How would you say it?

Target Market(s)

home owners wanting to add an outdoor space , new construction who need a back yard put in. People who have $5000 to $100,000 to spend on their yards

Industry/Entity Type

Construction

Requirements
Must have
• lots to say but how do we keep it peaceful and simple
• Every company shows a photo of a back yard they did. lets use food on a grill from Ravensbys grill site, a family around a gorgeous firepit or people enjoying life in their dream back yard. How can ours be different. we are not a pick up truck contractor. we have an amazing store showroom, craftsman to do the work and top brand name products and 30 year experienced designers. message we design and build. free estimates come see our store outdoor kitchens, pergolas, pavers, stone and more....
Nice to have
• professional look. we are an earth conscious company who cares about our planet, our customers and honors our people. i added a photo of one of our guys making a leaf inside a paver patio. i think it shows we are an artful paver construction company and showcases one of our craftsman.
Should not have
• i only posted a few photos but i think they are important. so words with no photos not so good. photos are available on web sites of our product manufacturer as well.

```html
<!DOCTYPE html>
<html lang="en">
<head>
<meta charset="utf-8">
<title>Solbrook Yard House – Flyer Front and Back</title>
<link rel="stylesheet" href="https://fonts.googleapis.com/css2?family=Arimo:wght@400;700&family=Comfortaa:wght@500;700&family=Open+Sans:wght@700;800&display=swap">
<style>
  :root{
    --page:#efe9df;
    --olive:#7f9a1f;
    --olive-dark:#5e7413;
    --olive-light:#b8cc4a;
    --lime:#c9d96a;
    --cream:#f4f6e6;
    --ink:#333333;
    --label:#3a2a14;
    --white:#ffffff;
  }
  *{box-sizing:border-box;margin:0;padding:0}
  html,body{width:1200px;height:900px;overflow:hidden;background:var(--page)}
  .canvas{position:relative;width:1200px;height:900px;font-family:"Arimo",Arial,sans-serif;color:var(--ink)}
  .side-label{position:absolute;top:14px;font-family:"Open Sans",Arial,sans-serif;font-weight:800;font-size:22px;letter-spacing:1px;color:var(--label)}
  .flyer{position:absolute;top:52px;height:825px;background:var(--cream);overflow:hidden;box-shadow:0 2px 8px rgba(0,0,0,.25)}
  .flyer-front{left:17px;width:566px}
  .flyer-back{left:600px;width:583px}
  .photo{position:absolute}
  .hero-photo{left:0;top:0;width:566px;height:520px;background:linear-gradient(180deg,#9cc3e6 0%,#d9e8f2 25%,#a07a4c 45%,#8b6a44 60%,#5f8a3a 80%,#4f7d2e 100%)}
  .band{position:absolute;left:0;width:100%}
  .round-photo{position:absolute;width:172px;height:172px;border-radius:50%;border:8px solid var(--olive-light);box-shadow:0 0 0 4px var(--white)}
  .grill-photo{left:80px;top:392px;background:radial-gradient(circle,#e19a3a 0%,#8a9a3a 45%,#2e2e2e 80%)}
  .statue-photo{left:308px;top:392px;background:radial-gradient(circle,#8d9488 0%,#6f8a4a 60%,#4b6a2a 100%)}
  .brand{position:absolute;display:flex;align-items:center;gap:8px}
  .brand-mark{width:50px;height:50px;border-radius:50%;background:var(--olive)}
  .brand-name{font-family:"Comfortaa",Arial,sans-serif;font-weight:700;color:var(--olive);line-height:.95}
  .brand-tag{position:absolute;font-family:"Arimo",Arial,sans-serif;font-weight:700;color:var(--olive-dark);white-space:nowrap}
  .front-brand{left:195px;top:60px}
  .front-brand .brand-name{font-size:25px}
  .front-tag{left:268px;top:113px;font-size:10px}
  .intro{position:absolute;left:26px;top:620px;width:520px;font-size:10.6px;line-height:1.33;color:var(--ink)}
  .family-photo{left:348px;top:688px;width:218px;height:137px;background:linear-gradient(160deg,#f2d2a8 0%,#e8b88a 40%,#6aa5d6 75%,#3f7fb8 100%);border-radius:40px 0 0 0}
  .front-footer{position:absolute;left:0;top:762px;width:566px;height:63px;background:linear-gradient(90deg,var(--olive-dark),var(--olive) 60%,var(--olive-light))}
  .contact{position:absolute;left:16px;color:var(--white);font-size:11.5px;display:flex;align-items:center;gap:5px}
  .contact svg{flex:none}
  .back-hero{left:0;top:0;width:583px;height:200px;background:linear-gradient(120deg,#c9ab7c 0%,#7a6a4e 30%,#5c4a36 55%,#8a7a66 75%,#6e6258 100%)}
  .section-title{position:absolute;left:36px;font-family:"Comfortaa",Arial,sans-serif;font-weight:700;font-size:17px;color:var(--olive);line-height:1.05}
  .list{position:absolute;left:36px;list-style:none}
  .list li{position:relative;padding-left:16px;font-size:13px;line-height:17.7px;color:var(--ink)}
  .list li::before{content:"";position:absolute;left:0;top:4px;width:9px;height:9px;border-radius:50%;background:var(--olive)}
  .framed{position:absolute;border:6px solid var(--lime);box-shadow:0 0 0 2px var(--white) inset}
  .pergola-photo{left:168px;top:324px;width:178px;height:160px;background:linear-gradient(180deg,#c9b48a 0%,#f0ead8 40%,#5f8f3a 75%,#4a7a2c 100%)}
  .fountain-photo{left:370px;top:220px;width:178px;height:166px;background:linear-gradient(180deg,#4f7a3a 0%,#8a7a5a 50%,#a7906a 100%)}
  .paver-photo{left:370px;top:406px;width:178px;height:168px;background:linear-gradient(180deg,#bfae96 0%,#a39076 55%,#8a7660 100%)}
  .back-brand{left:294px;top:698px}
  .back-brand .brand-name{font-size:18px}
  .back-brand .brand-mark{width:42px;height:42px}
  .back-tag{left:352px;top:742px;font-size:8px}
  .back-footer{position:absolute;left:0;top:776px;width:583px;height:49px;background:linear-gradient(90deg,var(--olive-dark),var(--olive) 50%,var(--olive-dark));color:var(--white);text-align:center}
  .call{font-family:"Comfortaa",Arial,sans-serif;font-weight:700;font-size:16px;padding-top:6px}
  .web{font-size:13px;margin-top:2px}
</style>
</head>
<body>
<div class="canvas">
  <div class="side-label" style="left:262px">FRONT</div>
  <div class="side-label" style="left:846px">BACK</div>

  <section class="flyer flyer-front">
    <div class="photo hero-photo" role="img" aria-label="Showroom pergola over a stone fountain with garden plants under a blue sky"></div>
    <svg class="band" style="top:380px" width="566" height="240" viewBox="0 0 566 240">
      <path d="M0 40 C150 140 380 170 566 115 L566 240 L0 240 Z" fill="var(--cream)"/>
      <path d="M0 40 C150 140 380 170 566 115 L566 145 C380 195 150 170 0 78 Z" fill="var(--olive-light)"/>
      <path d="M0 78 C150 170 380 195 566 145 L566 155 C380 207 150 182 0 90 Z" fill="var(--olive)"/>
    </svg>
    <div class="brand front-brand">
      <div class="brand-mark"></div>
      <div class="brand-name">SOLBROOK<br>YARD HOUSE</div>
    </div>
    <div class="brand-tag front-tag">YOUR FIREPLACE AND OUTDOOR LIVING COMPANY</div>
    <div class="round-photo grill-photo" role="img" aria-label="Grilled chicken and peppers in a cast iron pan"></div>
    <div class="round-photo statue-photo" role="img" aria-label="Stone head garden statues among plants"></div>
    <p class="intro">We are a backyard dream design and build out company. come to us with or without your plans and we will build it for you. What makes us unique is that we have a 21,000 square foot showroom with lots of fountains, outdoor kitchens, grills, paver showroom, yard art, rock and much more for you to see, feel and buy amazing stuff... we carry 100's of top brand products like stonavo, kestrow, gray pellman and heatvista products. we build pergolas, outdoor kitchens, firepits, fireplaces, water features and more.<br>our 3-d designs help you live it before you build it. but design is not our<br>main function, construction is. solbrookyardhouse.example has a 3-d<br>video on home page so you can see what we can do.</p>
    <div class="front-footer"></div>
    <div class="photo family-photo" role="img" aria-label="Smiling family of four lying together"></div>
    <div class="contact" style="top:778px">
      <svg width="10" height="13" viewBox="0 0 10 13"><path d="M5 0a5 5 0 0 1 5 5c0 3.5-5 8-5 8S0 8.5 0 5a5 5 0 0 1 5-5z" fill="var(--lime)"/><circle cx="5" cy="5" r="1.8" fill="var(--olive-dark)"/></svg>
      418 Alder Row, Brookfield Colorado
    </div>
    <div class="contact" style="top:797px">
      <svg width="12" height="12" viewBox="0 0 12 12"><path d="M2.5 0.5l2 2.5-1.2 1.4c.7 1.5 1.8 2.6 3.3 3.3L8 6.5l2.5 2-1 2.5C5 11 1 7 0.5 2.5z" fill="var(--lime)"/></svg>
      555-014-2277
      <svg width="11" height="11" viewBox="0 0 11 11" style="margin-left:6px"><circle cx="5.5" cy="5.5" r="5" fill="var(--lime)"/></svg>
      www.solbrookyardhouse.example
    </div>
  </section>

  <section class="flyer flyer-back">
    <div class="photo back-hero" role="img" aria-label="Cozy lodge living room with stone fireplace, armchairs and telescope"></div>
    <svg class="band" style="top:90px" width="583" height="130" viewBox="0 0 583 130">
      <path d="M0 130 L0 100 C200 60 400 80 583 25 L583 130 Z" fill="var(--cream)"/>
      <path d="M0 100 C200 60 400 80 583 25 L583 45 C400 98 200 74 0 114 Z" fill="var(--olive-light)"/>
      <path d="M0 114 C200 74 400 98 583 45 L583 53 C400 106 200 82 0 120 Z" fill="var(--olive)"/>
    </svg>

    <h2 class="section-title" style="top:232px">Come see our Indoor and Outdoor<br>showroom</h2>
    <ul class="list" style="top:272px">
      <li>Grills and Outdoor Kitchens</li><li>Pergolas</li><li>Fire Pits</li><li>Pavers</li><li>Stone</li><li>Fountains</li><li>Water Features</li><li>Lighting</li><li>Yard Art</li><li>Barn Doors</li>
    </ul>
    <h2 class="section-title" style="top:455px">Brands</h2>
    <ul class="list" style="top:478px">
      <li>Stonavo Pavers</li><li>Paveline Pavers</li><li>Gray Pellman Kitchens</li><li>Heatvista Grills</li><li>Norvale Grills</li><li>Alpenhearth Grills</li><li>Ravensby Grills</li><li>Taurro Grills</li><li>Kestrow Fiber glass Pergolas</li><li>Custom Cedar Pergolas</li>
    </ul>
    <h2 class="section-title" style="top:662px">Free Estimates</h2>
    <ul class="list" style="top:686px">
      <li>3-D Design available</li><li>Award winning designers</li><li>Traditional to Contemporary Design<br>and Install</li>
    </ul>

    <div class="framed pergola-photo" role="img" aria-label="Garden pergola with white curtains on a lawn"></div>
    <div class="framed fountain-photo" role="img" aria-label="Stacked stone urn fountain in a garden"></div>
    <div class="framed paver-photo" role="img" aria-label="Craftsman laying a leaf pattern in a paver patio"></div>

    <h2 class="section-title" style="top:588px;left:365px">Your Design or Ours</h2>
    <ul class="list" style="top:612px;left:368px">
      <li>We Install</li><li>30 years experience</li><li>Talented craftsman</li><li>As seen on HD TV</li>
    </ul>

    <div class="brand back-brand">
      <div class="brand-mark"></div>
      <div class="brand-name">SOLBROOK<br>YARD HOUSE</div>
    </div>
    <div class="brand-tag back-tag">YOUR FIREPLACE AND OUTDOOR LIVING COMPANY</div>

    <div class="back-footer">
      <div class="call">Call Us : 555-014-2277</div>
      <div class="web">www.solbrookyardhouse.example</div>
    </div>
  </section>
</div>
</body>
</html>
```